Garden Design Flier

I would like a PDF of this half page A4 flier in soft green tones with dark green leaves.

Target Market(s)

Home owners and real estate agents

Font styles to use
Serif
Other font styles liked:
• Papyrus

Colors
acd136
9bcb3c
cadf82
fefdec

Requirements
Must have
• Green tones
Nice to have
• Leaves, vines, lawns
Should not have
• Open to ideas, but classic style

```html
<!DOCTYPE html>
<html lang="en">
<head>
<meta charset="utf-8">
<title>Verdant Row Gardens – Flier</title>
<link rel="stylesheet" href="https://fonts.googleapis.com/css2?family=Macondo&display=swap">
<style>
  :root {
    --stage: #ecece4;
    --paper: #ffffff;
    --olive-dark: #4a5a22;
    --text-dark: #1f1f17;
    --leaf-pale: #fefdec;
    --leaf-soft: #cadf82;
    --leaf-mid: #9bcb3c;
    --leaf-sage: #8f9a6a;
  }
  * { margin: 0; padding: 0; box-sizing: border-box; }
  html, body {
    width: 1200px; height: 901px; overflow: hidden;
    background: var(--stage);
  }
  .flier {
    position: absolute; left: 20px; top: 41px;
    width: 1160px; height: 818px;
    font-family: "Macondo", "Papyrus", fantasy;
    color: var(--olive-dark);
  }
  .foliage-backdrop {
    position: absolute; inset: 0;
    background:
      radial-gradient(ellipse at 8% 20%, rgba(155,203,60,.55), transparent 45%),
      radial-gradient(ellipse at 95% 40%, rgba(143,154,106,.6), transparent 45%),
      radial-gradient(ellipse at 20% 95%, rgba(172,209,54,.5), transparent 45%),
      radial-gradient(ellipse at 85% 95%, rgba(202,223,130,.7), transparent 45%),
      radial-gradient(ellipse at 50% 0%, rgba(143,154,106,.45), transparent 50%),
      linear-gradient(135deg, var(--leaf-pale), var(--leaf-soft));
  }
  .content-panel {
    position: absolute; left: 101px; top: 75px;
    width: 957px; height: 671px;
    background: var(--paper);
    border: 9px solid var(--olive-dark);
  }
  .line {
    position: absolute; left: 0; right: 0;
    text-align: center; white-space: nowrap;
  }
  .brand-name {
    top: 38px; font-size: 118px; line-height: 1;
    letter-spacing: 6px;
  }
  .brand-sub {
    top: 160px; font-size: 38px; line-height: 1;
    letter-spacing: 22px; padding-left: 22px;
  }
  .owner { top: 228px; font-size: 27px; color: var(--text-dark); }
  .credential { top: 274px; font-size: 23px; color: var(--text-dark); }
  .services { top: 348px; font-size: 46px; line-height: 1; }
  .services .dot {
    display: inline-block; width: 13px; height: 13px; border-radius: 50%;
    background: var(--olive-dark); margin: 0 14px 8px; vertical-align: middle;
  }
  .pitch {
    top: 436px; font-size: 23.5px; line-height: 39px; color: var(--text-dark);
  }
  .divider {
    position: absolute; left: 46px; right: 46px; top: 588px;
    height: 1.5px; background: var(--olive-dark);
  }
  .contact {
    top: 610px; font-size: 19px; color: var(--text-dark);
  }
  .contact .sep { margin: 0 24px; }
</style>
</head>
<body>
  <main class="flier">
    <div class="foliage-backdrop" role="img" aria-label="Watercolour pattern of soft green and sage leaves and vines"></div>
    <section class="content-panel">
      <h1 class="line brand-name">VERDANT ROW</h1>
      <p class="line brand-sub">GARDENS</p>
      <p class="line owner">by LIAM HARWOOD</p>
      <p class="line credential">Certificate 3. Horticulture, Valley College</p>
      <p class="line services">Design<span class="dot"></span>Install<span class="dot"></span>Grow<span class="dot"></span>Tend<span class="dot"></span>Enjoy</p>
      <p class="line pitch">All your gardening and landscaping needs from design<br>and installation to general maintenance. Bespoke vegetable gardens<br>and potager designs created to suit your site and requirements</p>
      <div class="divider"></div>
      <p class="line contact">email: liam@verdantrowgardens.com.au<span class="sep">|</span>Call : 0400-123456<span class="sep">|</span>ABN: 12345678901</p>
    </section>
  </main>
</body>
</html>
```